Vision, Mission and Culture Posters

We have written text paragraphs for our company vision and mission and need them made into a2 or a3 sized posters using our logo for inspiration for colour. Our company culture has 10 paragraphs and we'd like this to be a single poster of a2 or a1. Each poster should have the logo on and share common design. It's not a complex job really.

Industry/Entity Type

It Company

Requirements
Nice to have
• These will be going up on our office wall so need to be clear to read from a distance and look professional but also not stodgy.

```html
<!DOCTYPE html>
<html lang="en">
<head>
<meta charset="utf-8">
<title>Vision Poster – Kerbside Bay Hire</title>
<link rel="stylesheet" href="https://fonts.googleapis.com/css2?family=Alfa+Slab+One&family=Anton&family=Archivo+Black&family=Archivo:wght@700&family=Josefin+Slab:wght@100;200&display=swap">
<style>
  :root {
    --brand-yellow: #ffec00;
    --brand-red: #d0191f;
    --ink: #0a0a0a;
    --paper: #f7f7f5;
    --paper-edge: #f3e9a6;
    --white: #ffffff;
  }
  html, body {
    margin: 0;
    padding: 0;
    width: 849px;
    height: 1200px;
    overflow: hidden;
    background: var(--paper);
  }
  .poster {
    position: relative;
    width: 849px;
    height: 1200px;
    overflow: hidden;
    background: radial-gradient(ellipse 62% 58% at 50% 52%, var(--paper) 70%, var(--paper-edge) 130%);
  }
  .poster__frame {
    position: absolute;
    inset: 0;
  }
  .brand {
    position: absolute;
    left: 60px;
    top: 31px;
    width: 352px;
    height: 102px;
    box-sizing: border-box;
    border: 4px solid var(--ink);
    border-radius: 12px;
    background: var(--brand-yellow);
    display: flex;
    align-items: center;
    gap: 22px;
    padding-left: 18px;
  }
  .brand__mark {
    width: 56px;
    height: 56px;
    background: var(--brand-red);
    flex: none;
  }
  .brand__name {
    font-family: "Archivo", Arial, sans-serif;
    font-weight: 700;
    font-size: 27px;
    line-height: 1.15;
    color: var(--ink);
    margin: 0;
  }
  .poster-title {
    position: absolute;
    left: 448px;
    top: 31px;
    width: 306px;
    height: 102px;
    margin: 0;
    border-radius: 12px;
    background: var(--ink);
    color: var(--brand-yellow);
    font-family: "Anton", Impact, sans-serif;
    font-weight: 400;
    font-size: 96px;
    line-height: 102px;
    text-align: center;
    letter-spacing: 1px;
  }
  .statement {
    position: absolute;
    inset: 0;
  }
  .t-thin { font-family: "Josefin Slab", Georgia, serif; font-weight: 100; fill: var(--ink); stroke: var(--ink); stroke-width: 0.6; }
  .t-condensed { font-family: "Anton", Impact, sans-serif; fill: var(--ink); }
  .t-red { fill: var(--brand-red); }
  .t-slab { font-family: "Alfa Slab One", Georgia, serif; fill: var(--brand-yellow); stroke: var(--ink); stroke-width: 3; paint-order: stroke; }
  .t-outline { font-family: "Archivo Black", Arial, sans-serif; fill: var(--white); stroke: var(--ink); stroke-width: 4; paint-order: stroke; }
</style>
</head>
<body>
<main class="poster">
  <svg class="poster__frame" width="849" height="1200" viewBox="0 0 849 1200" aria-hidden="true">
    <path d="M0 0 H849 V100 C820 112 805 130 782 150 C770 160 760 164 740 165 L0 154 Z" fill="var(--brand-yellow)"/>
    <path d="M0 1148 C200 1144 600 1146 820 1148 C840 1149 849 1160 849 1175 V1200 H0 Z" fill="var(--brand-red)"/>
  </svg>

  <div class="brand">
    <span class="brand__mark"></span>
    <p class="brand__name">Kerbside Bay<br>Hire</p>
  </div>
  <h1 class="poster-title">VISION</h1>

  <svg class="statement" width="849" height="1200" viewBox="0 0 849 1200" role="text"
       aria-label="To provide the most hassle-free parking rental service whilst giving a personal customer experience people want to tell their friends about">
    <text class="t-thin" x="72" y="338" font-size="116" textLength="685" lengthAdjust="spacingAndGlyphs">TO PROVIDE</text>
    <text class="t-condensed" x="0" y="0" font-size="105" textLength="323" lengthAdjust="spacingAndGlyphs"
          transform="translate(169 673) rotate(-90)">THE MOST</text>
    <text class="t-slab" x="189" y="447" font-size="108" textLength="568" lengthAdjust="spacingAndGlyphs">HASSLE-FREE</text>
    <text class="t-condensed t-red" x="193" y="671" font-size="238" textLength="560" lengthAdjust="spacingAndGlyphs">PARKING</text>
    <text class="t-outline" x="80" y="757" font-size="92" textLength="676" lengthAdjust="spacingAndGlyphs">RENTAL SERVICE</text>
    <text class="t-condensed" x="81" y="840" font-size="76" textLength="676" lengthAdjust="spacingAndGlyphs">WHILST GIVING A PERSONAL</text>
    <text class="t-slab" x="80" y="900" font-size="57" textLength="679" lengthAdjust="spacingAndGlyphs">CUSTOMER EXPERIENCE</text>
    <text class="t-condensed" x="81" y="1007" font-size="110" textLength="269" lengthAdjust="spacingAndGlyphs">PEOPLE</text>
    <text class="t-condensed" x="358" y="948" font-size="40" textLength="399" lengthAdjust="spacingAndGlyphs">WANT TO TELL THEIR</text>
    <text class="t-condensed t-red" x="358" y="1007" font-size="57" textLength="399" lengthAdjust="spacingAndGlyphs">FRIENDS ABOUT</text>
  </svg>
</main>
</body>
</html>
```